We are requiring some nice job add posters for hiring boilermakers or Fitters.
We would like the add to be supplied in a format that we can easily update and change text depending on the situation and details etc,
The job is specific to mining, so pictures in the background that could potentially be used could involve Washplant, draglines, excavators, electric shovel, dozer, actions shots of welding / grinding etc

I have attached some screenshots of adds I have seen recently that stand out.

Our company is QUORIN ENGINEERING SERVICES PTY LTD.

We would like on the add
CONTACT NUMBER - 0417 683 254
EMAIL admin@ quorinengineering.com.au

Some things we could highlight

Full time Position
Own Work Vehicle
Flexible Roster
Local Harbourline Company

```html
<!DOCTYPE html>
<html lang="en">
<head>
<meta charset="utf-8">
<title>Quorin Engineering – We Are Hiring Boilermakers</title>
<link rel="stylesheet" href="https://fonts.googleapis.com/css2?family=Bebas+Neue&family=Montserrat:wght@500;600;700&display=swap">
<style>
  :root {
    --green: #21cd8e;
    --navy: #26304a;
    --white: #ffffff;
    --photo-dark: #1c2230;
    --photo-warm: #5a4a2e;
    --photo-blue: #2b4a7a;
  }
  * { margin: 0; padding: 0; box-sizing: border-box; }
  html, body { width: 1196px; height: 1200px; overflow: hidden; background: var(--white); }
  .poster {
    position: relative;
    width: 1196px;
    height: 1200px;
    font-family: "Montserrat", sans-serif;
    overflow: hidden;
  }
  .header-band {
    position: absolute; left: 0; top: 0; width: 100%; height: 240px;
    background: var(--green);
    text-align: center;
  }
  .kicker {
    position: absolute; left: 0; right: 0; top: 30px;
    font-weight: 600; font-size: 47px; letter-spacing: 0.5px;
    color: var(--white); line-height: 1;
  }
  .role-title {
    position: absolute; left: 0; right: 0; top: 84px;
    font-family: "Bebas Neue", sans-serif;
    font-size: 168px; line-height: 1; letter-spacing: 4px;
    color: var(--navy);
  }
  .hero-photo {
    position: absolute; left: 0; top: 240px; width: 100%; height: 853px;
    background:
      radial-gradient(ellipse at 18% 70%, rgba(160,170,190,0.55) 0%, rgba(90,74,46,0.4) 25%, transparent 55%),
      radial-gradient(ellipse at 75% 45%, var(--photo-blue) 0%, transparent 45%),
      linear-gradient(90deg, var(--photo-warm) 0%, var(--photo-dark) 45%, #11151e 100%);
  }
  .benefits {
    position: absolute; left: 40px; top: 312px; list-style: none;
  }
  .benefits li {
    position: relative; padding-left: 40px;
    font-weight: 700; font-size: 47px; line-height: 90px;
    color: var(--white); letter-spacing: 0.3px;
  }
  .benefits li::before {
    content: ""; position: absolute; left: 0; top: 33px;
    width: 24px; height: 24px; border-radius: 50%;
    background: var(--green);
  }
  .panels { position: absolute; left: 0; top: 0; width: 1196px; height: 1200px; }
  .contact-label {
    position: absolute; left: 185px; top: 905px;
    font-weight: 600; font-size: 44px; color: var(--green); line-height: 1;
  }
  .contact-phone {
    position: absolute; left: 32px; top: 975px;
    font-weight: 600; font-size: 86px; color: var(--white); line-height: 1; letter-spacing: 1px;
  }
  .company-name {
    position: absolute; right: 18px; top: 985px; width: 440px;
    font-weight: 600; font-size: 30px; line-height: 48px;
    color: var(--white); text-align: right;
  }
  .footer-band {
    position: absolute; left: 0; top: 1093px; width: 100%; height: 107px;
    background: var(--green);
    display: flex; align-items: center; justify-content: center;
  }
  .contact-email {
    font-weight: 600; font-size: 52px; color: var(--navy); letter-spacing: 0.5px;
  }
</style>
</head>
<body>
<main class="poster">
  <div class="hero-photo" role="img" aria-label="Background photo of a welder in protective helmet and workwear welding steel with sparks flying"></div>

  <header class="header-band">
    <p class="kicker">WE ARE HIRING</p>
    <h1 class="role-title">BOILERMAKERS</h1>
  </header>

  <ul class="benefits">
    <li>FULL TIME POSITION</li>
    <li>OWN WORK VEHICLE</li>
    <li>FLEXIBLE ROSTER</li>
    <li>LOCAL HARBOURLINE COMPANY</li>
  </ul>

  <svg class="panels" viewBox="0 0 1196 1200" aria-hidden="true">
    <path class="contact-panel" d="M0 1093 V853 H640 Q700 853 735 920 L820 1093 Z" fill="var(--navy)"/>
    <path class="company-panel" d="M700 1093 L1196 825 V1093 Z" fill="var(--green)"/>
  </svg>

  <p class="contact-label">Contect Us</p>
  <p class="contact-phone">0417 683 254</p>
  <p class="company-name">QUORIN ENGINEERING SERVICES PTY LTD.</p>

  <footer class="footer-band">
    <p class="contact-email">admin@quorinengineering.com.au</p>
  </footer>
</main>
</body>
</html>
```